Tess Marlowe Communication business card

I am starting a small, country-based business that offers writing, communication and marketing services to a wide range of clients, inner city big business, to mining, through to agriculture.

The appeal of my business is that it's mobile and flexible. It's just me, with lots of hands-on experience on construction and infrastructure projects.

I can provide the following services:

• Communication planning and management
• Issues and media management
• Marketing and communication materials
• Project management and strategy
• Government liaison
• Incident management communication
• Stakeholder management

It would be great to be able to use the elements of the business card design on other stationery.

Industry/Entity Type

Communication

Requirements
Must have
• The following information:

Tess Marlowe
M: 0427 391 864
E: tess@tmcommsmail.com

PO Box 152
Durrandale Q 4472
Nice to have
• a rural element (windmill, workboots, wheat stalk)

```html
<!DOCTYPE html>
<html lang="en">
<head>
<meta charset="utf-8">
<title>Tess Marlowe Communication – Business Card</title>
<link rel="stylesheet" href="https://fonts.googleapis.com/css2?family=Marcellus+SC&display=swap">
<style>
  :root {
    --backdrop: #b0b0b0;
    --card: #ffffff;
    --ink: #2a2a2e;
    --navy: #27304f;
    --rule: #3a3a3a;
  }
  * { margin: 0; padding: 0; box-sizing: border-box; }
  html, body {
    width: 1200px;
    height: 900px;
    overflow: hidden;
    background: var(--backdrop);
  }
  .canvas {
    position: relative;
    width: 1200px;
    height: 900px;
    font-family: "Marcellus SC", "Times New Roman", serif;
    color: var(--ink);
  }
  .card {
    position: absolute;
    left: 330px;
    width: 536px;
    height: 346px;
    background: var(--card);
    text-align: center;
  }
  .card--front { top: 58px; }
  .card--back  { top: 466px; }

  .brand-dot {
    position: absolute;
    left: 50%;
    border-radius: 50%;
    background: var(--navy);
    transform: translateX(-50%);
  }
  .card--front .brand-dot { top: 52px; width: 22px; height: 22px; }
  .card--back  .brand-dot { top: 26px; width: 12px; height: 12px; }

  .brand-name {
    position: absolute;
    left: 0;
    right: 0;
    color: var(--ink);
    font-weight: 400;
    white-space: nowrap;
  }
  .card--front .brand-name { top: 128px; font-size: 29px; letter-spacing: 0.5px; }
  .card--back  .brand-name { top: 58px;  font-size: 13px; letter-spacing: 0.3px; }

  .person-name {
    position: absolute;
    left: 0; right: 0;
    top: 146px;
    font-size: 32px;
    letter-spacing: 1px;
  }
  .address {
    position: absolute;
    left: 0; right: 0;
    top: 208px;
    font-size: 16px;
    line-height: 20px;
    letter-spacing: 0.6px;
  }
  .contact {
    position: absolute;
    left: 0; right: 0;
    top: 266px;
    font-size: 16px;
    line-height: 19px;
    letter-spacing: 0.6px;
  }
  .contact .email { font-size: 14px; }

  .base-rule {
    position: absolute;
    left: 62px;
    width: 412px;
    height: 10px;
  }
  .card--front .base-rule { top: 310px; }
  .card--back  .base-rule { top: 314px; }
</style>
</head>
<body>
<div class="canvas">

  <section class="card card--front">
    <span class="brand-dot"></span>
    <div class="brand-name">Tess Marlowe Communication</div>
    <svg class="base-rule" viewBox="0 0 412 10" aria-hidden="true">
      <path d="M0 9 L206 8.4 L412 9 L206 9.6 Z" fill="var(--rule)"/>
      <path d="M62 4.5 L206 3.6 L350 4.5 L206 5.4 Z" fill="var(--rule)"/>
    </svg>
  </section>

  <section class="card card--back">
    <span class="brand-dot"></span>
    <div class="brand-name">Tess Marlowe Communication</div>
    <h1 class="person-name" style="font-weight:400">Tess Marlowe</h1>
    <p class="address">PO Box 152<br>Durrandale Q 4472</p>
    <p class="contact">0427 391 864<br><span class="email">tess@tmcommsmail.com</span></p>
    <svg class="base-rule" viewBox="0 0 412 10" aria-hidden="true">
      <path d="M0 5 L206 4.4 L412 5 L206 5.6 Z" fill="var(--rule)"/>
      <path d="M62 1.5 L206 0.7 L350 1.5 L206 2.3 Z" fill="var(--rule)"/>
    </svg>
  </section>

</div>
</body>
</html>
```